Coral Wing Flights brochure

A single A4 brochures that is tri-folded and shows some of our tour packages with contact details.

Please visit www.coralwingflights.com.au to see the designs and images that can be used.

I want to provide designers the freedom to try something creative because I want to give prospective client - normally tourists to Sydney a quality service. I want the brochure to reflect this.

The image on the front page needs to be of the Sydney Harbour. The image MUST be in daylight - not night time.

I have now provided an image of the aircraft (in GIF format). Please use this image and place it over the image of the harbour arch crossing and harbourside concert hall.

I may need to discuss this further but what I have not show in the attached files is a small form I will like the client to fill out..

Reservation number
Name
Address
Phone number
Email

We can discuss this at a latter time.

The QR Code needs to contain your web address (www.coralwingflights.com.au)

Target Market(s)

Visitors and tourists to Sydney who want a day trip.
We are providing an exciting way to see Sydney. By air in a light aircraft...

Industry/Entity Type

House

Font styles to use
Sans Serif
Script

Colors
33a6d7
3276b5
85acd3
85cae6
ffffff

Requirements
Must have
• Brochure must be A4 (with about 2 to 3mm bleed - so it can be cut at the printers). They but be folded in 3 to produce a DL size brochure.

The words "Prepare to be amazed" should be in script font...

Please use the following wording for our Terms can conditions...

Terms and Conditions
Coral Wing Flights operates from Pellham Field within Sydney’s busy airspace Your chosen flight may be subject to delays. Clearance to enter controlled airspace may be refused - this is especially true of our popular Coastline Panorama flight. If this happens, we can either offer other suitable flights, reschedule the flight or, if this isn’t suitable, we provide a refund.
Other aircraft, besides our standard Falcor Trekkers, are available if we consider they better suit your requirements.
See our web site www.coralwingflights.com.au for full details.
Coral Wing Flights is a trading name of Brightmere Pty Limited
(ABN 71 408 226 519) which operates under the Air Operators Certificate (AOC) of Durrow and Fitzgale Pty Ltd.
Nice to have
• Suggestion - on one of the sides (with the packages) to have a background image.

Suggestion is to keep the brochure light and "airy"

```html
<!DOCTYPE html>
<html lang="en">
<head>
<meta charset="utf-8">
<title>Coral Wing Flights – Tour Packages</title>
<link href="https://fonts.googleapis.com/css2?family=Arimo:wght@400;700&display=swap" rel="stylesheet">
<style>
  :root {
    --sea-deep: #1f5f93;
    --sea-mid: #3276b5;
    --sea-light: #85acd3;
    --sky: #85cae6;
    --panel: rgba(236, 242, 250, 0.88);
    --steel: #8fb0c0;
    --navy: #0f1626;
    --ink: #111111;
    --white: #ffffff;
    --green: #2e9e3e;
  }
  * { box-sizing: border-box; margin: 0; padding: 0; }
  html, body { width: 1200px; height: 1000px; overflow: hidden; }
  body { font-family: "Arimo", Arial, sans-serif; background: var(--white); }
  .brochure {
    position: relative; width: 1200px; height: 1000px; overflow: hidden;
    background: linear-gradient(180deg, var(--sky) 0%, var(--sea-light) 30%, var(--sea-mid) 70%, var(--sea-deep) 100%);
  }
  .backdrop { position: absolute; inset: 0; }
  .photo {
    position: absolute; border: 6px solid var(--white);
  }
  .photo--harbour { left: 38px; top: 43px; width: 336px; height: 311px;
    background: linear-gradient(180deg, #3f7fc8 0%, #6a8aa3 35%, #3d6b4a 55%, #14406e 100%); }
  .photo--coast { left: 430px; top: 43px; width: 342px; height: 281px;
    background: linear-gradient(180deg, #3f8fd8 0%, #cfe3f2 30%, #5b7a55 50%, #1d5a9a 62%, #0d3f80 100%); }
  .photo--mountains { left: 824px; top: 43px; width: 338px; height: 311px;
    background: linear-gradient(180deg, #5a86b5 0%, #a88f78 30%, #b86a34 55%, #5a3a1e 80%, #2f2418 100%); }

  .package { position: absolute; color: var(--ink); }
  .package__title { font-size: 17px; text-decoration: underline; text-underline-offset: 3px; font-weight: 400; }
  .package__duration { font-size: 17px; margin-top: 24px; }
  .package__stops { list-style: none; margin-top: 28px; }
  .package__stops li { display: flex; align-items: flex-start; font-size: 17px; line-height: 29.5px; }
  .package__stops svg { width: 20px; height: 20px; margin: 5px 12px 0 0; flex: none; }
  .package__stops .cont { padding-left: 32px; }
  .package--harbour { left: 62px; top: 427px; }
  .package--harbour .package__stops { padding-left: 16px; }
  .package--coastal { left: 455px; top: 382px; }
  .package--coastal .package__stops { padding-left: 14px; }
  .package--mountains { left: 845px; top: 427px; }
  .package--mountains .package__stops { padding-left: 18px; }

  .badge { position: absolute; width: 30px; height: 30px; }

  .terms { position: absolute; left: 80px; top: 788px; width: 1060px; color: var(--white); font-size: 12px; line-height: 15px; }
  .terms__title { display: block; width: max-content; margin: 0 auto 6px; padding: 1px 3px; border: 1.5px solid var(--white); font-size: 15px; font-weight: 400; }

  .price { position: absolute; top: 948px; display: flex; align-items: center; gap: 12px; color: var(--white); }
  .price__amount { border: 1.5px solid var(--white); padding: 1px 4px; font-size: 22px; line-height: 26px; }
  .price svg { width: 28px; height: 28px; }
  .price--harbour { left: 90px; }
  .price--coastal { left: 488px; }
  .price--mountains { left: 876px; }
</style>
</head>
<body>
<svg width="0" height="0" style="position:absolute">
  <defs>
    <symbol id="plane" viewBox="0 0 24 24">
      <path fill="#2a2a2a" d="M21 3.2c-.8-.8-2.2-.6-3 .2l-3.6 3.6-9.4-2.7-1.8 1.8 7.6 4.3-3.7 3.7-2.8-.5-1.4 1.4 3.4 1.8 1.8 3.4 1.4-1.4-.5-2.8 3.7-3.7 4.3 7.6 1.8-1.8-2.7-9.4 3.6-3.6c.8-.8 1-2.2.3-3z"/>
    </symbol>
    <symbol id="peaks" viewBox="0 0 30 30">
      <circle cx="15" cy="15" r="13" fill="#ffffff" stroke="#2e9e3e" stroke-width="3"/>
      <circle cx="15" cy="15" r="8.5" fill="#2e9e3e"/>
      <path fill="#ffffff" d="M8.5 19l4-6 2.5 3.5 2-2.5 4.5 5z"/>
    </symbol>
    <symbol id="dollar" viewBox="0 0 28 28">
      <circle cx="14" cy="14" r="13" fill="#ffffff"/>
      <circle cx="14" cy="14" r="10.5" fill="#2e9e3e"/>
      <text x="14" y="19.5" text-anchor="middle" font-family="Arimo, Arial, sans-serif" font-size="15" font-weight="700" fill="#ffffff">$</text>
    </symbol>
  </defs>
</svg>

<main class="brochure">
  <svg class="backdrop" width="1200" height="1000" viewBox="0 0 1200 1000" role="img" aria-label="Aerial view of the harbour and water as a background image">
    <rect x="0" y="0" width="1200" height="45" fill="var(--steel)"/>
    <polygon points="70,13 355,13 350,36 75,36" fill="var(--navy)"/>
    <polygon points="465,13 752,13 746,36 470,36" fill="var(--navy)"/>
    <polygon points="862,13 1168,13 1162,36 868,36" fill="var(--navy)"/>
    <line x1="400" y1="0" x2="400" y2="1000" stroke="rgba(255,255,255,0.35)" stroke-width="1"/>
    <line x1="797" y1="0" x2="797" y2="1000" stroke="rgba(255,255,255,0.35)" stroke-width="1"/>
    <polygon points="0,366 378,366 408,340 775,340 800,366 1200,366 1200,772 800,772 775,748 408,748 378,772 0,772"
             fill="var(--panel)" stroke="var(--white)" stroke-width="4"/>
    <rect x="0" y="940" width="1200" height="60" fill="var(--sea-deep)"/>
    <rect x="0" y="958" width="1200" height="22" fill="var(--steel)" opacity="0.8"/>
    <polygon points="50,942 362,942 350,988 62,988" fill="var(--navy)"/>
    <polygon points="445,942 760,942 748,988 457,988" fill="var(--navy)"/>
    <polygon points="835,942 1160,942 1148,988 847,988" fill="var(--navy)"/>
  </svg>

  <div class="photo photo--harbour" role="img" aria-label="Aerial photo of the city skyline with the harbourside concert hall"></div>
  <div class="photo photo--coast" role="img" aria-label="Aerial photo of the Sydney coastline and cliffs"></div>
  <div class="photo photo--mountains" role="img" aria-label="Photo of the Three Sisters rock formation in the Blue Mountains at sunset"></div>

  <svg class="badge" style="left:341px;top:414px"><use href="#peaks"/></svg>
  <svg class="badge" style="left:738px;top:371px"><use href="#peaks"/></svg>
  <svg class="badge" style="left:1121px;top:416px"><use href="#peaks"/></svg>

  <section class="package package--harbour">
    <h2 class="package__title">SYDNEY HARBOUR SCENIC</h2>
    <p class="package__duration">1 HOUR 20 MINS</p>
    <ul class="package__stops">
      <li><svg><use href="#plane"/></svg>Parramatta City</li>
      <li><svg><use href="#plane"/></svg>Hornsby</li>
      <li><svg><use href="#plane"/></svg>Bahai Temple</li>
      <li><svg><use href="#plane"/></svg>Long Reef</li>
      <li><svg><use href="#plane"/></svg>Habour Bridge &amp; Opera House</li>
      <li><svg><use href="#plane"/></svg>Manly</li>
    </ul>
  </section>

  <section class="package package--coastal">
    <h2 class="package__title">SYDNEY COASTAL</h2>
    <p class="package__duration">1 HOUR 20 MINS</p>
    <ul class="package__stops">
      <li><svg><use href="#plane"/></svg>Campbelltown.</li>
      <li><svg><use href="#plane"/></svg>Stanwell Park.</li>
      <li><svg><use href="#plane"/></svg>Entrance of Port Hacking.</li>
      <li><svg><use href="#plane"/></svg>Entrance of Botany Bay.</li>
      <li><svg><use href="#plane"/></svg>Sydney Beaches - Maroubra,</li>
      <li class="cont">Coogee,Bondi &amp; manly.</li>
      <li><svg><use href="#plane"/></svg>Sydney Heads</li>
      <li><svg><use href="#plane"/></svg>Long Reef</li>
    </ul>
  </section>

  <section class="package package--mountains">
    <h2 class="package__title">THE BLUE MOUNTAINS</h2>
    <p class="package__duration">1 HOUR 10 MINS</p>
    <ul class="package__stops">
      <li><svg><use href="#plane"/></svg>Katoomba</li>
      <li><svg><use href="#plane"/></svg>The Three Sisters</li>
      <li><svg><use href="#plane"/></svg>Warragamba Dam</li>
      <li><svg><use href="#plane"/></svg>Prospect Reservoir</li>
    </ul>
  </section>

  <section class="terms">
    <h3 class="terms__title">TERMS AND CONDITIONS</h3>
    <p>Coral Wing Flights operates from Pellham Field within Sydney’s busy airspace.Your chosen flight may be subject to delays.</p>
    <p>Clearance to enter controlled airspace may be refused- this is especially true of our popular Coastline Panorama flight.If this happens, we can offer other suitable flights, reschedule the flight or, if this is'nt suitable, we provide a refund.Other aircraft, besides our standard Falcor Trekkers, are available if consider they better suit your requirements.</p>
    <p>See our website www.coralwingflights.com.au for full details.</p>
    <p>Coral Wing Flights is a trading name of Brightmere Pty Limited (ABN 71 408 226 519) which operates under the Air Operators Certificate (AOC) of Durrow and Fitzgale Pty Ltd.</p>
  </section>

  <div class="price price--harbour"><svg><use href="#dollar"/></svg><span class="price__amount">$560 per aircraft</span></div>
  <div class="price price--coastal"><svg><use href="#dollar"/></svg><span class="price__amount">$560 per aircraft</span></div>
  <div class="price price--mountains"><svg><use href="#dollar"/></svg><span class="price__amount">$475 per aircraft</span></div>
</main>
</body>
</html>
```